ebook cover for quick turnaround: simple and statement with some design modification and inspirat...

Under Pale Moss is second in a series about Marla Quint's spirituality. We are looking for a design to complement the first, which is attached. Nothing cheesy, nothing too bold, and something more feminine. Colours must be the same: white background, same exact red, and so on. Under Pale Moss implies Under Pale Moss that is drunk while doing spiritual and mystical work, and is also a catchphrase of the book. The font should be different as the designer likes, but subtitle and author name font the same as book one. The image here is the letter X from the board game Tilvoran, and we ask that the designer put it at an angle and somehow adds a sense of the light that flashes through the tin on the We Rode North cover. Perhaps underneath the X?

Book info:
Title: Under Pale Moss
Subtitle: Archangel Michael Shows Himself
Image: Tilvoran X
Author: Marla Quint, PhD
Strap quote: "Her work with angels has permanently changed my life, especially her work with the Archangel Michael," Harriet Lusk, RN, BSN - Healer

```html
<!DOCTYPE html>
<html lang="en">
<head>
<meta charset="utf-8">
<title>Under Pale Moss — Marla Quint Ph.D.</title>
<link rel="stylesheet" href="https://fonts.googleapis.com/css2?family=Bebas+Neue&family=Montserrat:wght@300;400;600&display=swap">
<style>
  :root {
    --page-bg: #c9d0d2;
    --cover-white: #ffffff;
    --title-red: #b0111a;
    --ink: #1f1f1f;
    --ink-soft: #4a4a4a;
    --tile-light: #e8cfa8;
    --tile-dark: #c9a57a;
    --flash-core: #fff4ec;
    --flash-glow: #e0302a;
  }
  * { margin: 0; padding: 0; box-sizing: border-box; }
  html, body {
    width: 1200px;
    height: 989px;
    overflow: hidden;
    background: var(--page-bg);
  }
  .canvas {
    position: relative;
    width: 1200px;
    height: 989px;
  }
  .cover {
    position: absolute;
    left: 303px;
    top: 44px;
    width: 594px;
    height: 900px;
    background: var(--cover-white);
    text-align: center;
  }
  .cover > * {
    position: absolute;
    left: 0;
    right: 0;
    margin: 0 auto;
  }
  .strap-quote {
    top: 24px;
    font-family: "Montserrat", sans-serif;
    font-weight: 600;
    font-size: 10px;
    line-height: 1.7;
    color: var(--ink);
    text-transform: uppercase;
    white-space: nowrap;
  }
  .title {
    top: 70px;
    font-family: "Bebas Neue", sans-serif;
    font-weight: 400;
    font-size: 96px;
    line-height: 1;
    color: var(--title-red);
    text-transform: uppercase;
    white-space: nowrap;
  }
  .subtitle {
    top: 190px;
    font-family: "Montserrat", sans-serif;
    font-weight: 400;
    font-size: 26px;
    line-height: 1.4;
    letter-spacing: 0.2em;
    color: var(--ink);
    text-transform: uppercase;
    white-space: nowrap;
  }
  .tile-art {
    top: 380px;
    width: 340px;
    height: 340px;
  }
  .author {
    top: 800px;
    font-family: "Montserrat", sans-serif;
    font-weight: 300;
    font-size: 34px;
    letter-spacing: 0.05em;
    color: var(--ink-soft);
    text-transform: uppercase;
    white-space: nowrap;
  }
  .author .degree {
    text-transform: none;
    font-variant: small-caps;
  }
</style>
</head>
<body>
  <main class="canvas">
    <article class="cover">
      <p class="strap-quote">"Her work with angels has permanently changed my life, especially her work with<br>the Archangel Michael," Harriet Lusk, RN, BSN - Healer</p>
      <h1 class="title">Under Pale Moss</h1>
      <p class="subtitle">Archangel Michael<br>Shows Himself</p>
      <svg class="tile-art" viewBox="0 0 340 340" role="img" aria-label="Wooden Tilvoran letter tile showing the letter X, set at an angle, with a red-white flash of light glowing beneath it">
        <defs>
          <linearGradient id="tile-wood" x1="0" y1="0" x2="1" y2="1">
            <stop offset="0" stop-color="var(--tile-light)"/>
            <stop offset="1" stop-color="var(--tile-dark)"/>
          </linearGradient>
          <radialGradient id="flash-glow" cx="0.5" cy="0.5" r="0.5">
            <stop offset="0" stop-color="var(--flash-core)" stop-opacity="1"/>
            <stop offset="0.35" stop-color="var(--flash-glow)" stop-opacity="0.55"/>
            <stop offset="1" stop-color="var(--flash-glow)" stop-opacity="0"/>
          </radialGradient>
        </defs>
        <ellipse class="flash" cx="180" cy="290" rx="150" ry="34" fill="url(#flash-glow)" transform="rotate(-8 180 290)"/>
        <rect class="tile" x="45" y="40" width="250" height="260" rx="10" fill="url(#tile-wood)" transform="rotate(-8 170 170)"/>
      </svg>
      <p class="author">Marla Quint <span class="degree">Ph.D.</span></p>
    </article>
  </main>
</body>
</html>
```